Darrow Consulting needs a quality & professional business card!

I am a recruitment and employment consultant from Brisbane, Australia and I had a fantastic logo organised by this community to I am hoping the business card will be the same.

I have attached the Darrow consulting logo that ideally would feature on the back of the business card. There are a number of logos for you to use as you see fit. I would like the colour cheme to match that of the Darrow Consulting logo. I also have a secondary company called Career Lantern Australia and I have included that logo as well. While it is an important part of the business I don't want this logo feature too predominantly as I am moving out of this space. This logo was created by myself and is of low quality. Feel free to use the icon and words however you want. The winning design will be smart, professional and eye-catching.

The information I am looking for in the business card is:
Name: Gavin Darrow
Position: Founder & Director
Phone: (07) 3519 6482
Mobile: 0431 586 207
Email: gavin@careerlantern.com.au

Target Market(s)

Recruiters, government, large companies

Contact Information for Business Card

Name: Gavin Darrow
Phone: (07) 3519 6482
Mobile: 0431 586 207
Web: www.careerlantern.com.au

Font styles to use
Serif
Sans Serif

Requirements
Must have
• Darrow Consulting Logo on reverse side
• Contact details on front side with smaller reference to Darrow Consulting logo and Career Lantern Australia logo

```html
<!DOCTYPE html>
<html lang="en">
<head>
<meta charset="utf-8">
<title>Darrow Consulting — Business Card</title>
<link href="https://fonts.googleapis.com/css2?family=Montserrat:wght@500;600&family=Open+Sans:wght@400;500&display=swap" rel="stylesheet">
<style>
  :root {
    --backdrop: #1f1f20;
    --card-dark: #141414;
    --card-light: #ffffff;
    --ink: #222325;
    --muted: #8a8b8d;
    --brand-blue: #0a8fd0;
    --brand-green: #0ea34a;
    --brand-orange: #e4862c;
    --brand-charcoal: #2a2c2f;
    --white: #ffffff;
  }
  * { box-sizing: border-box; margin: 0; padding: 0; }
  html, body {
    width: 1200px; height: 900px; overflow: hidden;
    background: var(--backdrop);
  }
  .canvas {
    width: 1200px; height: 900px;
    display: flex; flex-direction: column; align-items: center; justify-content: center;
    gap: 36px;
  }
  .card {
    position: relative;
    width: 700px; height: 400px;
    overflow: hidden;
    box-shadow: 0 10px 30px rgba(0,0,0,.45);
  }

  /* Reverse side */
  .card--back {
    background: radial-gradient(circle at 85% 80%, #2e2e2f 0%, var(--card-dark) 60%);
  }
  .back-brand {
    position: absolute; left: 0; right: 0; top: 160px;
    display: flex; align-items: center; justify-content: center; gap: 18px;
  }
  .back-brand__mark {
    width: 34px; height: 34px; background: var(--white);
  }
  .back-brand__name {
    font-family: "Montserrat", sans-serif; font-weight: 500;
    font-size: 40px; letter-spacing: 1px; color: var(--white);
    text-transform: uppercase; white-space: nowrap;
  }
  .partner {
    position: absolute; right: 34px; bottom: 30px;
    display: flex; align-items: center; gap: 10px;
  }
  .partner__mark {
    width: 30px; height: 30px; border-radius: 50%; background: #3a3a3c;
  }
  .partner__name {
    font-family: "Montserrat", sans-serif; font-weight: 600;
    font-size: 16px; color: var(--white); white-space: nowrap;
  }

  /* Front side */
  .card--front { background: var(--card-light); }
  .front-brand {
    position: absolute; left: 44px; top: 150px;
    width: 330px;
    display: flex; align-items: center; gap: 12px;
  }
  .front-brand__mark {
    width: 24px; height: 24px; background: var(--ink); flex: none;
  }
  .front-brand__name {
    font-family: "Montserrat", sans-serif; font-weight: 500;
    font-size: 22px; letter-spacing: .3px; color: var(--ink);
    text-transform: uppercase; white-space: nowrap;
  }
  .divider {
    position: absolute; left: 395px; top: 100px;
    width: 2px; height: 120px; background: var(--brand-blue);
  }
  .contact {
    position: absolute; left: 420px; top: 100px; right: 20px;
  }
  .contact__name {
    font-family: "Montserrat", sans-serif; font-weight: 600;
    font-size: 27px; color: var(--brand-blue); text-transform: uppercase;
    line-height: 1; white-space: nowrap;
  }
  .contact__role {
    font-family: "Open Sans", sans-serif; font-weight: 500;
    font-size: 16px; color: var(--ink); margin-top: 4px; letter-spacing: .4px;
  }
  .contact__list { list-style: none; margin-top: 10px; }
  .contact__item {
    display: flex; align-items: center; gap: 12px;
    font-family: "Open Sans", sans-serif; font-size: 16px; color: var(--ink);
    line-height: 24px; letter-spacing: .3px; white-space: nowrap;
  }
  .contact__icon { width: 12px; height: 12px; flex: none; }
  .colour-band {
    position: absolute; left: 0; right: 0; bottom: 0; height: 12px;
    display: flex;
  }
  .colour-band span { flex: 1; }
  .colour-band .blue { background: var(--brand-blue); }
  .colour-band .green { background: var(--brand-green); }
  .colour-band .orange { background: var(--brand-orange); }
  .colour-band .charcoal { background: var(--brand-charcoal); }
</style>
</head>
<body>
<main class="canvas">
  <section class="card card--back" aria-label="Card reverse">
    <div class="back-brand">
      <span class="back-brand__mark"></span>
      <span class="back-brand__name">Darrow Consulting</span>
    </div>
    <div class="partner">
      <span class="partner__mark"></span>
      <span class="partner__name">Career Lantern Australia</span>
    </div>
  </section>

  <section class="card card--front" aria-label="Card front">
    <div class="front-brand">
      <span class="front-brand__mark"></span>
      <span class="front-brand__name">Darrow Consulting</span>
    </div>
    <div class="divider"></div>
    <div class="contact">
      <h1 class="contact__name">Gavin Darrow</h1>
      <p class="contact__role">Founder &amp; Director</p>
      <ul class="contact__list">
        <li class="contact__item">
          <svg class="contact__icon" viewBox="0 0 12 12" fill="none" stroke="var(--brand-blue)" stroke-width="1.4"><rect x="3" y="1" width="6" height="10" rx="1"/></svg>
          (07) 3519 6482
        </li>
        <li class="contact__item">
          <svg class="contact__icon" viewBox="0 0 12 12" fill="var(--brand-blue)"><path d="M2 1.5 4 1l1.2 2.6-1.3 1a6 6 0 0 0 3 3l1-1.3L10.5 7.6 10 10a8.5 8.5 0 0 1-8-8.5z"/></svg>
          0431 586 207
        </li>
        <li class="contact__item">
          <svg class="contact__icon" viewBox="0 0 12 12" fill="none" stroke="var(--brand-blue)" stroke-width="1.3"><rect x="1" y="2.5" width="10" height="7"/><path d="M1 2.5 6 6.5 11 2.5"/></svg>
          gavin@careerlantern.com.au
        </li>
      </ul>
    </div>
    <div class="colour-band">
      <span class="blue"></span><span class="green"></span><span class="orange"></span><span class="charcoal"></span>
    </div>
  </section>
</main>
</body>
</html>
```